Vehicle Rental Hire in the Algarve - Portugal

We are opening a Vehicle Rental company in the Algarve - Portugal - this will attract both locals and Tourists visiting. So we want this website to capture the beautiful location we will be set in, along with the familiarity of a vehicle rental company. And to keep a colour scheme in Line with out Logo. We are Marlenic Vehicle Rental.

Industry/Entity Type

Vehicle Rental

Number of Pages Required

1 page

Requirements
Must have
• must be professional, and simple to use navigation bar - must also have a "make a reservation" box - similar to the screenshot attached - Under our logo it must read "Vehicle Rental"
Nice to have
• It needs to be in a colour scheme that fits in with our logo

```html
<!DOCTYPE html>
<html lang="pt">
<head>
<meta charset="utf-8">
<title>Marlenic Vehicle Rental</title>
<link href="https://fonts.googleapis.com/css2?family=Outfit:wght@300;400;500;600;800&display=swap" rel="stylesheet">
<style>
:root{
  --hero:#4a3fd8;
  --hero-deep:#2d2496;
  --primary:#1c12dc;
  --field:#ecebfc;
  --ink:#1d1d2b;
  --band:#b73129;
  --band-deep:#a3271f;
  --white:#ffffff;
}
*{margin:0;padding:0;box-sizing:border-box}
html,body{width:1200px;height:946px;overflow:hidden;background:var(--white)}
body{position:relative;font-family:'Outfit',sans-serif;color:var(--ink)}
.abs{position:absolute}
.hero{left:0;top:0;width:1200px;height:755px;overflow:hidden;
  background:radial-gradient(ellipse at 30% 45%,#6d64e6 0%,#4d43d6 45%,#3a30c4 100%)}
.hero-shade{left:0;top:0;width:1200px;height:755px}
.logo{left:155px;top:14px;width:102px;height:102px;border:2px solid var(--white);border-radius:50%}
.logo-name{left:130px;top:44px;width:152px;text-align:center;color:var(--white);font-size:22px;font-weight:500;letter-spacing:.5px}
.logo-tag{left:130px;top:88px;width:152px;text-align:center;color:var(--white);font-size:7px;font-weight:500}
.nav a{position:absolute;top:55px;color:var(--white);font-size:15.5px;font-weight:500;text-decoration:none}
.nav-cta{left:954px;top:44px;width:105px;height:43px;border-radius:22px;background:var(--white);color:var(--primary);font-size:15.5px;display:flex;align-items:center;justify-content:center;font-weight:500}
.headline{left:139px;top:245px;color:var(--white);font-size:37px;font-weight:800;line-height:57px;letter-spacing:-.2px}
.sub{left:142px;top:434px;color:var(--white);font-size:21px;font-weight:400}
.deal{left:142px;color:var(--white);font-size:21px;text-decoration:underline;text-underline-offset:5px;text-decoration-thickness:1px}
.hero-cta{left:142px;top:577px;width:104px;height:42px;border-radius:21px;background:var(--white);color:var(--primary);font-size:15.5px;display:flex;align-items:center;justify-content:center}
.card{left:731px;top:140px;width:321px;height:567px;background:var(--white);border-radius:21px}
.card-title{left:0;top:27px;width:321px;text-align:center;color:var(--primary);font-size:15px;font-weight:600}
.card-rule{left:144px;top:56px;width:32px;height:3px;border-radius:2px;background:var(--primary)}
.lbl{font-size:11.5px;color:var(--ink)}
.field{height:35px;border-radius:18px;background:var(--field);font-size:11.5px;color:#3a3a4a;display:flex;align-items:center;padding-left:14px}
.field svg{position:absolute;right:13px;top:12px}
.check{left:30px;top:164px;color:var(--primary);font-size:11.5px;display:flex;align-items:center;gap:6px}
.search{left:31px;top:502px;width:104px;height:43px;border-radius:22px;background:var(--primary);color:var(--white);font-size:15px;font-weight:500;display:flex;align-items:center;justify-content:center}
.band{left:0;top:755px;width:1200px;height:136px;background:linear-gradient(135deg,var(--band) 0%,#c13a30 50%,var(--band-deep) 100%)}
.agent{left:141px;top:692px;width:145px;height:199px;border-radius:70px 70px 0 0;background:linear-gradient(180deg,#c98a3a 0%,#d9922c 60%,#b87524 100%)}
.support-title{left:300px;top:795px;color:var(--white);font-size:21px;font-weight:600}
.support-phone{left:301px;top:831px;color:var(--white);font-size:12.5px;display:flex;align-items:center;gap:6px}
.news-title{left:752px;top:782px;color:var(--white);font-size:17px;font-weight:600}
.news-input{left:753px;top:819px;width:306px;height:41px;border-radius:21px;background:var(--white);font-size:11.5px;color:#333;display:flex;align-items:center;padding-left:15px}
.news-input svg{position:absolute;right:14px;top:11px}
.footer{left:0;top:908px;width:1200px;text-align:center;font-size:15px;font-weight:500;color:var(--ink)}
</style>
</head>
<body>
<div class="abs hero" role="img" aria-label="Fotografia de carrinhas brancas estacionadas com filtro azul"></div>
<svg class="abs hero-shade" viewBox="0 0 1200 755" aria-hidden="true">
  <polygon points="820,140 1200,0 1200,755 560,755" fill="#2d2496" opacity=".55"/>
</svg>

<div class="abs logo"></div>
<div class="abs logo-name">Marlenic</div>
<div class="abs logo-tag">Vehicle Rental</div>

<nav class="nav">
  <a style="left:587px">Sobre nós</a>
  <a style="left:683px">Promoções</a>
  <a style="left:790px">Veículos</a>
  <a style="left:876px">Serviços</a>
</nav>
<div class="abs nav-cta">Contato</div>

<h1 class="abs headline">Aluguer De Automóveis<br>No Aeroporto De Faro -<br>Não Há Queixas Connosco!</h1>
<p class="abs sub">Reserve Agora Ou Contacte-nos</p>
<p class="abs deal" style="top:483px">Obtenha O Melhor Negócio!</p>
<p class="abs deal" style="top:522px">Aeroporto De Faro, RESERVE JA!</p>
<div class="abs hero-cta">Contato</div>

<section class="abs card">
  <h2 class="abs card-title">Fazer uma reserva</h2>
  <div class="abs card-rule"></div>

  <div class="abs lbl" style="left:30px;top:87px">Local de retirada</div>
  <div class="abs field" style="left:31px;top:113px;width:268px">Por favor escolha...
    <svg width="12" height="8" viewBox="0 0 12 8"><path d="M1 1l5 5 5-5" fill="none" stroke="#222" stroke-width="1.6"/></svg></div>

  <div class="abs check">
    <svg width="19" height="19" viewBox="0 0 19 19"><circle cx="9.5" cy="9.5" r="8.5" fill="none" stroke="#1c12dc" stroke-width="1.2"/><path d="M5.5 9.8l2.7 2.7 5.3-6" fill="none" stroke="#1c12dc" stroke-width="1.3"/></svg>
    Local de retirada igual ao local de retorno</div>

  <div class="abs lbl" style="left:30px;top:197px">Idade do motorista</div>
  <div class="abs field" style="left:31px;top:223px;width:268px">Por favor escolha...
    <svg width="12" height="8" viewBox="0 0 12 8"><path d="M1 1l5 5 5-5" fill="none" stroke="#222" stroke-width="1.6"/></svg></div>

  <div class="abs lbl" style="left:30px;top:271px">Categoria do veículo</div>
  <div class="abs field" style="left:31px;top:297px;width:268px">Todos
    <svg width="12" height="8" viewBox="0 0 12 8"><path d="M1 1l5 5 5-5" fill="none" stroke="#222" stroke-width="1.6"/></svg></div>

  <div class="abs lbl" style="left:30px;top:345px">Data de retirada</div>
  <div class="abs lbl" style="left:176px;top:345px">Hora</div>
  <div class="abs field" style="left:31px;top:371px;width:122px">dd-mm-aaaa</div>
  <div class="abs field" style="left:177px;top:371px;width:121px">9:00
    <svg width="12" height="8" viewBox="0 0 12 8"><path d="M1 1l5 5 5-5" fill="none" stroke="#222" stroke-width="1.6"/></svg></div>

  <div class="abs lbl" style="left:30px;top:420px">Data de entrega</div>
  <div class="abs lbl" style="left:176px;top:420px">Hora</div>
  <div class="abs field" style="left:31px;top:446px;width:122px">dd-mm-aaaa</div>
  <div class="abs field" style="left:177px;top:446px;width:121px">9:00
    <svg width="12" height="8" viewBox="0 0 12 8"><path d="M1 1l5 5 5-5" fill="none" stroke="#222" stroke-width="1.6"/></svg></div>

  <div class="abs search">Procurar</div>
</section>

<div class="abs band"></div>
<div class="abs agent" role="img" aria-label="Fotografia de uma assistente de apoio ao cliente ao telefone"></div>
<div class="abs support-title">Suporte ao cliente</div>
<div class="abs support-phone">
  <svg width="12" height="12" viewBox="0 0 24 24"><path d="M6.6 10.8a15 15 0 006.6 6.6l2.2-2.2a1 1 0 011-.25 11.4 11.4 0 003.6.57 1 1 0 011 1V20a1 1 0 01-1 1A17 17 0 013 4a1 1 0 011-1h3.5a1 1 0 011 1c0 1.25.2 2.45.57 3.6a1 1 0 01-.25 1z" fill="#fff"/></svg>
  210-555-0147</div>
<div class="abs news-title">Subscrever A Newsletter</div>
<div class="abs news-input">Por favor escreva seu e-mail
  <svg width="20" height="18" viewBox="0 0 20 18"><path d="M1 8L19 1l-5 16-4-6z" fill="#b73129"/><path d="M10 11l9-10" stroke="#fff" stroke-width="1"/></svg></div>

<footer class="abs footer">© 2024 Marlenic Aluguel de veículos. Todos os direitos reservados.</footer>
</body>
</html>
```